Advertising agency needs site design

You will be designing a clean (plenty of white space) and vivid (colorful) design that is for an advertising agency named Brightwell Reach. Their current web site is located at www.BrightwellReach.net. From there you can see their services and get a feel for the company as the site stands today.
The following are direct quotes from the client:
“I want a clean look with colors of the teal blue, deep yellow (in logo) and then a good energetic orange (deep orange - rich) should bring a good feel and enthusiasm.”
“The orange can be a nice accent color, not dominant.”
“Saw two other things I like - the website lanternkitestudio.com was pretty cool. I liked how the top banner changed colors as you moved to different tabs. I am somewhat wanting the colors I mentioned - like the blue color we use can be lighter as long as it works with the logo. - love the tulip forge site. I want quirky, creative and clean look - fun feel but slightly sophisticated to work with the medical field.”
Brightwell Reach currently focuses on the following primary industries:
• Medical / Health Care – Currently the primary industry
• Retail Industry
• Automotive Industry
• Entertainment Industry
Primary Services
• Media Planning & Buying: Web, TV, Print, Radio
• Campaign monitoring and reporting
• Commercial Production: TV & Radio
• Strategic Planning
• Market Research
• Internet Marketing: Email, SEO, Web design / development
Primary Navigation will consist of the following:
• Home
• About Us
o History
o Principal Profile (sub nav)
o Sales Team & Partners
• Clients
• Services
• Testimonials
• Contact Us
They want the web site to act as a basis for future marketing collateral so the overall feel from the web site must be capable of translating to print and other collateral. I do not currently have a clean digital version of their logo however their logo is on the web site (brightwellreach.net)
Reason: Still awaiting feedback from client on designs. They should be back to us shortly.
Target Market(s)
larger companies that are purchasing air time on television and radio. Typically in the health care industry and others described above in brief.
Industry/Entity Type
Advertising
Look and feel
Each slider illustrates characteristics of the customer's brand and the style your logo design should communicate.

```html
<!DOCTYPE html>
<html lang="en">
<head>
<meta charset="utf-8">
<title>About Brightwell Reach</title>
<link href="https://fonts.googleapis.com/css2?family=Arimo:wght@400&display=swap" rel="stylesheet">
<style>
  :root {
    --band-teal: #0e3a4a;
    --band-teal-light: #127a8f;
    --accent-gold: #f2a900;
    --accent-orange: #e8561c;
    --text-grey: #6a6a6a;
    --nav-grey: #3a3a3a;
    --soft-grey: #a8a8a8;
    --page-white: #ffffff;
  }
  * { margin: 0; padding: 0; box-sizing: border-box; }
  html, body {
    width: 1200px;
    height: 900px;
    overflow: hidden;
    background: var(--page-white);
    font-family: "Arimo", Arial, sans-serif;
  }
  .page { position: relative; width: 1200px; height: 900px; }

  .top-band {
    position: absolute; left: 0; top: 0;
    width: 1200px; height: 60px;
    background: var(--band-teal);
    border-bottom: 4px solid var(--accent-orange);
    transition: background-color 0.3s ease;
  }
  .page:has(.nav-home:hover) .top-band { background: var(--band-teal-light); }
  .page:has(.nav-about:hover) .top-band,
  .page:has(.nav-history:hover) .top-band,
  .page:has(.nav-profile:hover) .top-band,
  .page:has(.nav-team:hover) .top-band { background: var(--band-teal); }
  .page:has(.nav-clients:hover) .top-band { background: #b87f00; }
  .page:has(.nav-services:hover) .top-band { background: var(--accent-orange); }
  .page:has(.nav-testimonials:hover) .top-band { background: #0f6e63; }
  .page:has(.nav-contact:hover) .top-band { background: #c9441a; }

  .brand-mark {
    position: absolute; left: 40px; top: 19px;
    width: 18px; height: 18px;
    background: var(--accent-gold);
  }
  .brand-name {
    position: absolute; left: 68px; top: 10px;
    color: var(--page-white);
    font-size: 30px; font-weight: 400;
    letter-spacing: 1px; line-height: 36px;
  }

  .contact-lines {
    position: absolute; right: 54px; top: 72px;
    text-align: right;
    font-size: 12px; line-height: 12px;
    color: var(--nav-grey);
  }
  .contact-lines .value { color: var(--accent-gold); }

  .main-nav {
    position: absolute; left: 0; top: 137px;
    width: 1200px; height: 20px;
    font-size: 12px; line-height: 14px; color: var(--nav-grey);
  }
  .main-nav span {
    position: absolute; top: 0; white-space: nowrap;
    padding-bottom: 3px; border-bottom: 2px solid transparent;
  }
  .main-nav span:hover { color: var(--accent-orange); }
  .main-nav .is-current { color: var(--accent-orange); border-bottom-color: var(--accent-gold); }

  .showcase-panel { position: absolute; top: 174px; height: 262px; }
  .panel-left { left: 40px; width: 312px; background: linear-gradient(180deg, #d9e6ea 0%, #eef3f4 55%, #9fc6cf 100%); }
  .panel-centre { left: 364px; width: 610px; background: linear-gradient(180deg, #e4e8e9 0%, #f4f6f6 50%, #cfd8d6 82%, #8fb069 100%); }
  .panel-right { left: 994px; width: 158px; background: linear-gradient(180deg, #e1e4e4 0%, #f3f4f4 60%, #d0d4d4 100%); }

  .about-section { position: absolute; left: 344px; top: 462px; width: 732px; }
  .about-title {
    color: var(--accent-gold);
    font-size: 28px; font-weight: 400;
    line-height: 34px; margin-bottom: 20px;
  }
  .about-section p {
    color: var(--text-grey);
    font-size: 12.5px; line-height: 16px;
    margin-bottom: 16px;
  }

  .site-footer {
    position: absolute; left: 40px; top: 810px;
    color: var(--soft-grey);
    font-size: 12px; line-height: 15px;
  }
</style>
</head>
<body>
<div class="page">
  <header class="top-band">
    <div class="brand-mark"></div>
    <div class="brand-name">Brightwell Reach</div>
  </header>

  <div class="contact-lines">
    <div>telephone : <span class="value">214.555.0148</span></div>
    <div>email: <span class="value">info@brightwellreach.net</span></div>
  </div>

  <nav class="main-nav">
    <span class="nav-home" style="left:44px">home</span>
    <span class="nav-about is-current" style="left:100px">about us</span>
    <span class="nav-history" style="left:172px">history</span>
    <span class="nav-profile" style="left:234px">principal profile</span>
    <span class="nav-team" style="left:344px">sales team and partners</span>
    <span class="nav-clients" style="left:496px">clients</span>
    <span class="nav-services" style="left:556px">services</span>
    <span class="nav-testimonials" style="left:628px">testimonials</span>
    <span class="nav-contact" style="left:718px">contact us</span>
  </nav>

  <div class="showcase-panel panel-left" role="img" aria-label="Bright white interior with a wall aquarium"></div>
  <div class="showcase-panel panel-centre" role="img" aria-label="White lounge with wall-mounted television, potted palms and green floor strip"></div>
  <div class="showcase-panel panel-right" role="img" aria-label="Corner of a white room with a low white seat"></div>

  <main class="about-section">
    <h1 class="about-title">about Brightwell Reach</h1>
    <p>Our long-standing relationships with the media give us stronger buying clout and broader opportunities than many of our competitors. And, we make it our business to stay on top of promotional and cooperative opportunities, passing incredible savings and increased exposure to you!</p>
    <p>Over 20 years in the media and marketing industries positions us to deliver the results our clients depend upon.</p>
    <p>Brightwell Reach, Inc. has developed a talented pool of strategic partners and combined them to provide a full range of services, making us a single source for all your marketing needs.</p>
    <p>We conceptualize and strategize.Through extensive research services and software providing quantitative and qualitative information, we'll create smart, targeted and cost-effective media plans. Implementation, monitoring and review of the plan's impact are included in the fee for that service.</p>
    <p>Our commitment to the client's needs and concerns always comes first. We offer personal attention and deliver positive results that increase your bottom line.</p>
  </main>

  <footer class="site-footer">
    <div>Copyright 2011 Brightwell Reach.</div>
  </footer>
</div>
</body>
</html>
```